Singer/songwriter needs a catchy design for new folk/rock single

This will be used for promotion of the single on streaming platforms: eg. Tunewell Stream, Sonora, etc. This song is quirky with a folk rock twist. It's basically one long metaphor of a guy who may/or may not have cheated on his girlfriend and she 'hits him with her car'. The song is titled Left On the Porch. Artist name is Dale Warrington. Please incorporate the song title and artist text using one of the uploaded images. Vintage feel gets bonus points. Song is included for your listening 'enjoyment'.

```html
<!DOCTYPE html>
<html lang="en">
<head>
<meta charset="utf-8">
<title>Left On the Porch – Dale Warrington</title>
<link rel="stylesheet" href="https://fonts.googleapis.com/css2?family=Playfair+Display:wght@500&family=Lobster&display=swap">
<style>
  :root {
    --cyan: #2fd6e6;
    --cyan-light: #bff4f8;
    --cyan-shade: #0f8fa0;
    --magenta: #c85ed0;
    --magenta-light: #f2c4f2;
    --magenta-shade: #7a2c86;
    --silver: #d6d6d0;
    --silver-shade: #5c5c58;
    --photo-top: #b9aea3;
    --photo-mid: #4a3f39;
    --photo-deep: #1b1618;
  }
  html, body {
    margin: 0;
    width: 1200px;
    height: 1200px;
    overflow: hidden;
    background: var(--photo-deep);
  }
  .cover {
    position: relative;
    width: 1200px;
    height: 1200px;
    overflow: hidden;
  }
  .cover-photo {
    position: absolute;
    inset: 0;
    background:
      radial-gradient(circle at 34% 50%, rgba(190,170,150,0.55) 0 14%, rgba(90,75,65,0.4) 22%, transparent 32%),
      linear-gradient(90deg, transparent 55%, rgba(200,200,205,0.18) 60%, transparent 63%, rgba(200,200,205,0.18) 70%, transparent 74%, rgba(200,200,205,0.15) 82%, transparent 86%),
      linear-gradient(180deg, var(--photo-top) 0%, #7c7068 10%, var(--photo-mid) 30%, #2e2629 65%, var(--photo-deep) 100%);
  }
  .title-line {
    position: absolute;
    margin: 0;
    font-family: "Playfair Display", "Bodoni Moda", serif;
    font-weight: 500;
    line-height: 1;
    white-space: nowrap;
    transform-origin: 0 0;
  }
  .title-top {
    left: 58px;
    top: 40px;
    font-size: 200px;
    letter-spacing: 6px;
    transform: scaleY(2.7);
    color: var(--cyan);
    background: linear-gradient(90deg, var(--cyan) 0%, var(--cyan-light) 55%, var(--cyan) 100%);
    -webkit-background-clip: text;
    background-clip: text;
    -webkit-text-fill-color: transparent;
    filter: drop-shadow(3px 2px 0 var(--cyan-shade)) drop-shadow(0 6px 6px rgba(0,0,0,0.45));
  }
  .title-bottom {
    left: 250px;
    top: 520px;
    font-size: 148px;
    letter-spacing: 4px;
    transform: scaleY(3.3);
    color: var(--magenta);
    background: linear-gradient(90deg, var(--magenta) 0%, var(--magenta-light) 60%, var(--magenta) 100%);
    -webkit-background-clip: text;
    background-clip: text;
    -webkit-text-fill-color: transparent;
    filter: drop-shadow(3px 2px 0 var(--magenta-shade)) drop-shadow(0 6px 6px rgba(0,0,0,0.45));
  }
  .artist {
    position: absolute;
    left: 48px;
    top: 890px;
    margin: 0;
    font-family: "Lobster", cursive;
    font-weight: 400;
    font-size: 92px;
    line-height: 0.95;
    color: var(--silver);
    text-shadow: 2px 3px 0 var(--silver-shade), 0 8px 12px rgba(0,0,0,0.55);
  }
  .artist span { display: block; }
  .artist .surname { padding-left: 30px; }
</style>
</head>
<body>
  <main class="cover">
    <div class="cover-photo" role="img" aria-label="Close-up photograph of a vintage car's chrome headlamp and vertical radiator grille"></div>
    <h1 class="title">
      <span class="title-line title-top">LEFT ON</span>
      <span class="title-line title-bottom">THE PORCH</span>
    </h1>
    <p class="artist"><span class="first">Dale</span><span class="surname">Warrington</span></p>
  </main>
</body>
</html>
```